Embed-able Video Player for Video Website

We need a new video player embed widget built for our membership video website. This is used by members to place our video content on other websites. You can see an example of the last one here:

https://vornaplex.example-host.net/darkdeck

You can see the video website here:

http://kestramoor.org/

It should have category icons with individual videos in each category section.

It needs to be built to be mobile responsive.. so please show both a desktop and mobile view side by side.

Having search bar is also a plus. I have attached a very old version as well that we really liked to give you ideas, the live version doesnt exist anymore.

To many designers did not read the brief and submitted invalid designs

• All Categories Listed, each category shows videos.. all catgories and videos are on kestramoor.org

```html
<!DOCTYPE html>
<html lang="en">
<head>
<meta charset="utf-8">
<title>Kestramoor Video Widget – Desktop and Mobile</title>
<link href="https://fonts.googleapis.com/css2?family=Montserrat:wght@300;400;600;700&family=Open+Sans:wght@300;400&display=swap" rel="stylesheet">
<style>
  :root{
    --board:#c1c1c1;
    --surface:#efefef;
    --card:#ffffff;
    --brand-red:#c8202f;
    --ink:#2f2f2f;
    --muted:#444444;
    --footer:#2e2e2e;
    --footer-ink:#ffffff;
  }
  *{box-sizing:border-box;margin:0;padding:0}
  html,body{width:1200px;height:761px;overflow:hidden}
  body{background:var(--board);position:relative;font-family:'Open Sans',sans-serif;color:var(--ink)}

  .view{position:absolute;background:var(--surface);overflow:hidden}
  .view--desktop{left:61px;top:38px;width:778px;height:642px}
  .view--mobile{left:874px;top:38px;width:280px;height:676px}

  .site-header{position:absolute;left:0;top:0;width:100%;height:56px;background:var(--surface)}
  .brand{position:absolute;font-family:'Montserrat',sans-serif;font-weight:700;color:var(--brand-red);letter-spacing:-0.5px;white-space:nowrap}
  .view--desktop .brand{left:46px;top:12px;font-size:27px}
  .view--mobile .brand{left:16px;top:16px;font-size:17px}

  .btn{position:absolute;display:flex;align-items:center;justify-content:center;border:1.5px solid var(--brand-red);border-radius:14px;background:#fff;color:var(--brand-red);font-family:'Montserrat',sans-serif;font-weight:600;white-space:nowrap}
  .view--desktop .btn{top:18px;width:98px;height:22px;font-size:9px}
  .view--desktop .btn--visit{left:531px}
  .view--desktop .btn--ask{left:634px}
  .view--mobile .btn{left:180px;width:85px;height:19px;font-size:7.5px}
  .view--mobile .btn--visit{top:6px}
  .view--mobile .btn--ask{top:30px}

  .hero{position:absolute;left:0;top:56px;width:100%;
    background:
      radial-gradient(circle at 50% 50%, rgba(230,120,110,.55) 0, rgba(200,60,70,.25) 12%, transparent 30%),
      radial-gradient(circle at 15% 30%, rgba(40,90,210,.45) 0, transparent 25%),
      radial-gradient(circle at 85% 70%, rgba(40,80,190,.4) 0, transparent 28%),
      linear-gradient(135deg,#0b1436 0%,#101c4a 45%,#0a1030 100%);
    display:flex;align-items:center;justify-content:center}
  .view--desktop .hero{height:259px}
  .view--mobile .hero{height:235px;align-items:flex-start;padding-top:94px}
  .hero-title{font-family:'Montserrat',sans-serif;color:#fff;font-size:24px;letter-spacing:.3px;white-space:nowrap}
  .hero-title strong{font-weight:700}
  .hero-title span{font-weight:300}
  .view--desktop .hero-title{margin-top:2px}

  .video-card{position:absolute;background:var(--card);box-shadow:0 1px 2px rgba(0,0,0,.18)}
  .thumb{position:relative;width:100%}
  .thumb--archaeology{background:linear-gradient(120deg,#8a6a48 0%,#5a4330 45%,#3a2a1e 100%)}
  .thumb--evolution{background:radial-gradient(circle at 78% 45%,#e6a5a2 0,#d98a86 30%,transparent 45%),linear-gradient(90deg,#a83c38,#c9605a)}
  .thumb--flood{background:linear-gradient(135deg,#4a4a4a 0%,#3a3b55 50%,#2b2f66 100%)}
  .thumb--science{background:linear-gradient(135deg,#c7c29e 0%,#a9a486 45%,#6f7066 100%)}
  .play{position:absolute;left:50%;top:50%;transform:translate(-50%,-50%)}

  .card-title{font-family:'Montserrat',sans-serif;font-weight:600;color:var(--ink);text-transform:uppercase;letter-spacing:.2px}
  .card-text{font-weight:300;color:var(--muted)}

  .view--desktop .video-card{top:355px;width:167px;height:174px}
  .view--desktop .thumb{height:113px}
  .view--desktop .card-title{position:absolute;left:17px;top:122px;font-size:11px}
  .view--desktop .card-text{position:absolute;left:16px;top:139px;font-size:8.4px;line-height:11px;width:145px}

  .view--mobile .video-card{width:123px;height:128px}
  .view--mobile .thumb{height:83px}
  .view--mobile .card-title{position:absolute;left:12px;top:91px;font-size:8.5px}
  .view--mobile .card-text{position:absolute;left:11px;top:103px;font-size:6px;line-height:8px;width:108px}

  .site-footer{position:absolute;left:0;width:100%;background:var(--footer);color:var(--footer-ink);font-family:'Montserrat',sans-serif;font-weight:400}
  .view--desktop .site-footer{top:574px;height:68px}
  .view--mobile .site-footer{top:605px;height:71px}
  .copyright{position:absolute;white-space:nowrap}
  .view--desktop .copyright{left:51px;top:16px;font-size:9.5px}
  .view--mobile .copyright{left:0;width:100%;text-align:center;top:18px;font-size:8px}
  .social{position:absolute;display:flex}
  .social li{list-style:none;border:1.5px solid #fff;border-radius:50%}
  .view--desktop .social{left:638px;top:15px;gap:3px}
  .view--desktop .social li{width:23px;height:23px}
  .view--mobile .social{left:102px;top:37px;gap:2px}
  .view--mobile .social li{width:19px;height:19px}
</style>
</head>
<body>

<section class="view view--desktop" aria-label="Desktop view">
  <header class="site-header">
    <div class="brand">kestramoor.org</div>
    <a class="btn btn--visit">Plan A Visit</a>
    <a class="btn btn--ask">Ask A Question</a>
  </header>
  <div class="hero" role="img" aria-label="Two hands reaching toward a glowing atom on a dark blue starry background">
    <h1 class="hero-title"><strong>SCIENCE</strong> <span>VIDEO</span></h1>
  </div>

  <article class="video-card" style="left:39px">
    <div class="thumb thumb--archaeology" role="img" aria-label="Presenter in a hat standing among ancient ruins">
      <svg class="play" width="28" height="28" viewBox="0 0 28 28"><circle cx="14" cy="14" r="14" fill="#fff"/><path d="M11 8l9 6-9 6z" fill="#111"/></svg>
    </div>
    <h2 class="card-title">Archaeology</h2>
    <p class="card-text">Featured:Does Archaeology Support the Bible?</p>
  </article>
  <article class="video-card" style="left:215px">
    <div class="thumb thumb--evolution" role="img" aria-label="Evolution silhouettes under a magnifying glass on red">
      <svg class="play" width="28" height="28" viewBox="0 0 28 28"><circle cx="14" cy="14" r="14" fill="#fff"/><path d="M11 8l9 6-9 6z" fill="#111"/></svg>
    </div>
    <h2 class="card-title">Evolution</h2>
    <p class="card-text">Featured:Does Archaeology Support the Bible?</p>
  </article>
  <article class="video-card" style="left:390px">
    <div class="thumb thumb--flood" role="img" aria-label="Speaker in a blue shirt in front of a rock wall">
      <svg class="play" width="28" height="28" viewBox="0 0 28 28"><circle cx="14" cy="14" r="14" fill="#fff"/><path d="M11 8l9 6-9 6z" fill="#111"/></svg>
    </div>
    <h2 class="card-title">Noah's Ark</h2>
    <p class="card-text">Featured:Was There a Global Flood?</p>
  </article>
  <article class="video-card" style="left:567px">
    <div class="thumb thumb--science" role="img" aria-label="Aerial view of eroded volcanic terrain">
      <svg class="play" width="28" height="28" viewBox="0 0 28 28"><circle cx="14" cy="14" r="14" fill="#fff"/><path d="M11 8l9 6-9 6z" fill="#111"/></svg>
    </div>
    <h2 class="card-title">Science</h2>
    <p class="card-text">Featured:What Can We Learn from Mount St. Helens?</p>
  </article>

  <footer class="site-footer">
    <p class="copyright">© 2020 Company Name | All Rights Reserved</p>
    <ul class="social" aria-label="Social links"><li></li><li></li><li></li><li></li></ul>
  </footer>
</section>

<section class="view view--mobile" aria-label="Mobile view">
  <header class="site-header">
    <div class="brand">kestramoor.org</div>
    <a class="btn btn--visit">Plan A Visit</a>
    <a class="btn btn--ask">Ask A Question</a>
  </header>
  <div class="hero" role="img" aria-label="Two hands reaching toward a glowing atom on a dark blue starry background">
    <h1 class="hero-title"><strong>SCIENCE</strong> <span>VIDEO</span></h1>
  </div>

  <article class="video-card" style="left:13px;top:308px">
    <div class="thumb thumb--archaeology" role="img" aria-label="Presenter in a hat standing among ancient ruins">
      <svg class="play" width="20" height="20" viewBox="0 0 28 28"><circle cx="14" cy="14" r="14" fill="#fff"/><path d="M11 8l9 6-9 6z" fill="#111"/></svg>
    </div>
    <h2 class="card-title">Archaeology</h2>
    <p class="card-text">Featured:Does Archaeology Support the Bible?</p>
  </article>
  <article class="video-card" style="left:143px;top:308px">
    <div class="thumb thumb--evolution" role="img" aria-label="Evolution silhouettes under a magnifying glass on red">
      <svg class="play" width="20" height="20" viewBox="0 0 28 28"><circle cx="14" cy="14" r="14" fill="#fff"/><path d="M11 8l9 6-9 6z" fill="#111"/></svg>
    </div>
    <h2 class="card-title">Evolution</h2>
    <p class="card-text">Featured:Does Archaeology Support the Bible?</p>
  </article>
  <article class="video-card" style="left:14px;top:443px">
    <div class="thumb thumb--flood" role="img" aria-label="Speaker in a blue shirt in front of a rock wall">
      <svg class="play" width="20" height="20" viewBox="0 0 28 28"><circle cx="14" cy="14" r="14" fill="#fff"/><path d="M11 8l9 6-9 6z" fill="#111"/></svg>
    </div>
    <h2 class="card-title">Noah's Ark</h2>
    <p class="card-text">Featured:Was There a Global Flood?</p>
  </article>
  <article class="video-card" style="left:144px;top:443px">
    <div class="thumb thumb--science" role="img" aria-label="Aerial view of eroded volcanic terrain">
      <svg class="play" width="20" height="20" viewBox="0 0 28 28"><circle cx="14" cy="14" r="14" fill="#fff"/><path d="M11 8l9 6-9 6z" fill="#111"/></svg>
    </div>
    <h2 class="card-title">Science</h2>
    <p class="card-text">Featured:What Can We Learn from Mount St. Helens?</p>
  </article>

  <footer class="site-footer">
    <p class="copyright">© 2020 Company Name | All Rights Reserved</p>
    <ul class="social" aria-label="Social links"><li></li><li></li><li></li><li></li></ul>
  </footer>
</section>

</body>
</html>
```